依頼詳細
・提案先は、「高圧受電設備(キュービクル)」を所有している(高圧電力を使用している)企業の社長様です。
例)食品加工や印刷所、鉄工所などの工場、ゴルフ場、ホテル、スポーツジム、介護施設など

・提案の主たる内容は、
「特許受付済みの全く新しい仕組みで、「高圧受電設備(キュービクル)」にかかる保管管理費用や修理修繕費用を完全『無料』にできる」
というものです。

・企業様の電力を担う内容になるためPOPさは必要なく、信頼が感じられるチラシを希望いたします。

・イラストレーターのデータでいただきたいです。
記載項目
株式会社青嶺工業、キュービクルアウトソーシング事業、特約店フェアリンク合同会社、ホームページURL(https://www.seireikougyo-ex.jp/)、4つの書類
サイズ
A4
ページ数
片面
希望イメージ
シンプル 複雑
単色 カラフル
暗い 明るい
日常 高級
遊び心 厳粛
未来的 伝統的
女性的 男性的
希望する色
緑系、青系
納品ファイル
• イラストレーター形式 (.ai)
補足説明
■ 選んだ理由

パッと見た印象で伝えたいことがとても強調されていて、とてもインパクトがあったので選ばせていただきました。

■ 提案者全員のお礼・コメント

初めてのクラフティオ利用だったので少し不安がありましたが、たくさんのとても素敵なご提案をありがとうございます。どれも素敵だったので選ぶのに時間がかかってしまいました。また何かありましたら依頼したいと思わせてもらったのはクラフティオさん達のおかげです。貴重なお時間を使い、作成していただき本当にありがとうございます。

```html
<!DOCTYPE html>
<html lang="ja">
<head>
<meta charset="utf-8">
<title>キュービクル コスト削減のご案内 | 株式会社青嶺工業</title>
<link rel="stylesheet" href="https://fonts.googleapis.com/css2?family=Noto+Sans+JP:wght@400;500;700;900&display=swap">
<style>
  :root {
    --green: #1f9a4a;
    --green-dark: #137a37;
    --sage: #7f9c8e;
    --ink: #333333;
    --ink-soft: #555555;
    --paper: #ffffff;
    --panel: #f1f3f2;
    --accent: #e8383d;
  }
  * { margin: 0; padding: 0; box-sizing: border-box; }
  html, body { width: 849px; height: 1200px; overflow: hidden; background: var(--paper); }
  body { font-family: "Noto Sans JP", sans-serif; color: var(--ink); }
  .flyer { position: relative; width: 849px; height: 1200px; overflow: hidden; background: var(--paper); }

  .hero-band {
    position: absolute; left: 0; top: 0; width: 849px; height: 150px;
    background: linear-gradient(180deg, var(--green) 0%, #3db36a 100%);
  }
  .hero-title {
    position: absolute; left: 0; top: 8px; width: 849px; text-align: center;
    font-size: 122px; font-weight: 900; color: var(--paper); letter-spacing: 6px; line-height: 1.1;
  }

  .cubicle-photo {
    position: absolute; left: 150px; top: 150px; width: 470px; height: 300px;
    background: radial-gradient(ellipse at 50% 55%, #e3e5e4 0%, #c7cbc9 60%, #f4f5f4 100%);
  }
  .person-photo {
    position: absolute; left: 600px; top: 330px; width: 249px; height: 380px;
    background: linear-gradient(180deg, #d9d4cf 0%, #4a4a52 45%, #2f2f36 100%);
  }

  .target-line {
    position: absolute; writing-mode: vertical-rl; white-space: nowrap;
    font-weight: 900; color: var(--green); line-height: 1; letter-spacing: 1px;
  }
  .target-line.first { left: 86px; top: 165px; font-size: 44px; }
  .target-line.second { left: 22px; top: 175px; font-size: 48px; }
  .target-line small { font-size: 26px; color: var(--green-dark); }
  .target-line .dark { color: #222; }

  .expert-bubble {
    position: absolute; left: 640px; top: 170px; width: 190px; height: 190px; border-radius: 50%;
    background: var(--paper); border: 4px solid var(--green);
    display: flex; flex-direction: column; align-items: center; justify-content: center;
    color: var(--green); font-weight: 900; text-align: center; line-height: 1.3;
  }
  .expert-bubble .big { font-size: 30px; }
  .expert-bubble .mid { font-size: 22px; color: var(--green-dark); }
  .expert-bubble .small { font-size: 18px; color: var(--ink); }

  .intro { position: absolute; left: 232px; top: 462px; width: 362px; }
  .intro-head {
    font-size: 16px; font-weight: 900; color: var(--green); white-space: nowrap;
    border-bottom: 3px solid var(--green); padding-bottom: 4px; line-height: 1.4;
  }
  .intro-head strong { font-size: 20px; color: var(--green-dark); }
  .intro-body { margin-top: 10px; font-size: 12.5px; line-height: 1.7; color: var(--ink-soft); }

  .checklist {
    position: absolute; left: 232px; top: 606px; width: 362px;
    border: 1.5px solid var(--sage); border-radius: 4px; padding: 8px 12px; background: var(--paper);
  }
  .checklist-title { font-size: 12.5px; font-weight: 700; color: var(--ink); text-align: center; margin-bottom: 4px; }
  .checklist li { list-style: none; display: flex; align-items: center; gap: 6px; font-size: 12px; line-height: 1.7; color: var(--ink-soft); }
  .checklist svg { flex: none; }

  .documents { position: absolute; left: 0; top: 730px; width: 849px; height: 300px; background: var(--panel); }
  .free-badge {
    position: absolute; left: 30px; top: 30px; width: 100px; height: 100px; border-radius: 50%;
    background: var(--green); color: var(--paper); font-weight: 900;
    display: flex; flex-direction: column; align-items: center; justify-content: center; line-height: 1.1;
  }
  .free-badge .s { font-size: 17px; }
  .free-badge .l { font-size: 30px; }
  .doc-head { position: absolute; left: 150px; top: 22px; color: var(--green); font-weight: 900; font-size: 56px; letter-spacing: 1px; line-height: 1.3; }
  .doc-lead { position: absolute; left: 150px; top: 100px; font-size: 20px; font-weight: 700; color: var(--ink); line-height: 1.45; }
  .doc-lead em { font-style: normal; color: var(--accent); }
  .doc-grid {
    position: absolute; left: 105px; top: 165px; width: 680px;
    display: grid; grid-template-columns: 1fr 1fr; gap: 12px 24px;
  }
  .doc-item {
    height: 40px; border-radius: 4px; background: var(--sage); color: var(--paper);
    font-size: 19px; font-weight: 700; display: flex; align-items: center; justify-content: center;
  }
  .doc-note { position: absolute; left: 0; top: 265px; width: 849px; text-align: center; font-size: 19px; font-weight: 700; color: var(--ink); }

  .contact-band {
    position: absolute; left: 0; top: 1030px; width: 849px; height: 30px;
    background: var(--green); color: var(--paper); text-align: center; font-size: 17px; font-weight: 700; line-height: 30px; letter-spacing: 4px;
  }

  .footer { position: absolute; left: 0; top: 1060px; width: 849px; height: 140px; }
  .brand { position: absolute; left: 28px; top: 22px; display: flex; align-items: center; gap: 10px; }
  .brand-dot { width: 40px; height: 40px; border-radius: 50%; background: var(--green); }
  .brand-name { font-size: 24px; font-weight: 700; color: var(--green); letter-spacing: 1px; }
  .company { position: absolute; left: 28px; top: 80px; font-size: 15px; font-weight: 700; color: var(--ink); }
  .company span { font-size: 11px; font-weight: 400; color: var(--ink-soft); margin-left: 8px; }
  .tel { position: absolute; left: 370px; top: 14px; display: flex; align-items: center; gap: 8px; color: var(--green); font-weight: 900; font-size: 44px; letter-spacing: 1px; }
  .tel-meta { position: absolute; left: 370px; top: 82px; font-size: 13px; color: var(--ink-soft); display: flex; gap: 28px; }
</style>
</head>
<body>
<main class="flyer">
  <div class="hero-band"></div>
  <h1 class="hero-title">コスト削減</h1>

  <div class="cubicle-photo" role="img" aria-label="屋外に設置された高圧受電設備キュービクルの写真"></div>
  <div class="person-photo" role="img" aria-label="資料を手にしたスーツ姿の女性スタッフの写真"></div>

  <p class="target-line first">キュービクル<small>（高圧受電設備）</small><span class="dark">を</span></p>
  <p class="target-line second">所有している企業様へ</p>

  <div class="expert-bubble">
    <span class="big">電力の</span>
    <span class="mid">エキスパートに</span>
    <span class="small">お任せください!</span>
  </div>

  <section class="intro">
    <h2 class="intro-head">管理コストを見直して<strong>大幅なコスト削減へ!</strong></h2>
    <p class="intro-body">キュービクルを設置されている企業様の「管理コスト（保安管理費用など）」の見直しを提案しております。全国での導入事例も多く、「コストの大幅な削減につながった」と大変喜んでいただいております。</p>
  </section>

  <section class="checklist">
    <p class="checklist-title">下記に当てはまる企業様はぜひお問い合わせください</p>
    <ul>
      <li><svg width="12" height="12" viewBox="0 0 12 12"><rect x="0.5" y="0.5" width="11" height="11" fill="none" stroke="#1f9a4a"/><path d="M2.5 6l2.5 2.5 4.5-5" fill="none" stroke="#1f9a4a" stroke-width="1.6"/></svg>キュービクル（高圧受電設備）を設置している</li>
      <li><svg width="12" height="12" viewBox="0 0 12 12"><rect x="0.5" y="0.5" width="11" height="11" fill="none" stroke="#1f9a4a"/><path d="M2.5 6l2.5 2.5 4.5-5" fill="none" stroke="#1f9a4a" stroke-width="1.6"/></svg>電気契約が高圧でキュービクルの所有者である</li>
      <li><svg width="12" height="12" viewBox="0 0 12 12"><rect x="0.5" y="0.5" width="11" height="11" fill="none" stroke="#1f9a4a"/><path d="M2.5 6l2.5 2.5 4.5-5" fill="none" stroke="#1f9a4a" stroke-width="1.6"/></svg>現在キュービクルの保守点検などの費用が負担である</li>
    </ul>
  </section>

  <section class="documents">
    <div class="free-badge"><span class="s">見積</span><span class="l">無料</span></div>
    <h2 class="doc-head">4つの書類</h2>
    <p class="doc-lead">を揃えていただくことで、<br><em>いくらコストが削減</em>できるかをお見積させていただけます。</p>
    <div class="doc-grid">
      <div class="doc-item">電気料金の請求書1年分</div>
      <div class="doc-item">保安管理費用明細</div>
      <div class="doc-item">キュービクル設備台帳</div>
      <div class="doc-item">単線結線図</div>
    </div>
    <p class="doc-note">お見積もりや導入の費用は一切かかりません！ お気軽にご相談ください。</p>
  </section>

  <div class="contact-band">お問い合わせ</div>

  <footer class="footer">
    <div class="brand"><span class="brand-dot"></span><span class="brand-name">SEIREI KOGYO</span></div>
    <p class="company">株式会社青嶺工業<span>特約店フェアリンク合同会社</span></p>
    <p class="tel">
      <svg width="36" height="36" viewBox="0 0 24 24"><path fill="#1f9a4a" d="M6.6 10.8a15.1 15.1 0 006.6 6.6l2.2-2.2a1 1 0 011-.25 11.4 11.4 0 003.6.57 1 1 0 011 1V20a1 1 0 01-1 1A17 17 0 013 4a1 1 0 011-1h3.5a1 1 0 011 1c0 1.25.2 2.45.57 3.6a1 1 0 01-.25 1z"/></svg>
      082-415-2786
    </p>
    <p class="tel-meta"><span>FAX : 082-415-2787</span><span>https://www.seireikougyo-ex.jp/</span></p>
  </footer>
</main>
</body>
</html>
```